■依頼の目的
2月に出版予定の電子書籍

タイトル:後悔しない住まい手配ガイド決定版2021
サブタイトル:[特集]三世代でつなぐ暮らし設計
著者:一級建築士 柚木湊

キャッチコピー:コロナ対応住宅チェックリスト付き!

※追加テキスト
家づくりの補助金
4月に省エネ説明義務化
IoT住宅の現在

キャッチコピー等の配置はPDFに記載

の表紙デザインをお願いします。

■本の内容
・年一回発行する雑誌形式の電子書籍
・住宅会社選びの方法を紹介
・特集記事や時事ネタも扱う

■デザイン要望
・30代~40代の子育て夫婦に好まれるデザインを希望
・LivoMarqueのようなお洒落な家づくり雑誌の雰囲気
・過去の4作品との差別化(過去表紙はPDFに)
・最新作であることがわかるよう「2021」を目立つように

■キャッチ等の変更の可能性あり
お願いする方が決まった後、キャッチコピーなどの文字を若干変更する可能性があります。

■添付ファイルについて
・必要な配置をPDFに添付しています
・ロゴのaiデータ添付します

その他何かご不明な点がございましたら、お気軽にご質問下さい。
よろしくお願いいたします。
・Pebble magazine というタイトルの色は、変えるようにしてください。
年一回の雑誌なので、毎年、ちがう色を使っています。
過去の作品と被らないように色提案をお願いします。
・文字はスマホで見た時にも、読めることを意識してください。
・背景の写真・イラストのセレクトが重要になります。livoなどのインテリア雑誌などを参考にしてください。

写真の選び方が秀逸でした。
シンメトリーを意識したモダンな建物外観が素晴らしく、それを引き立たせるようなデザインで、見た瞬間、これしかないと思わせるものでした。
今回は、私のメルマガ読者200人にアンケートを行って半数の方がこのデザインを支持しました。

この度は、沢山のご提案を頂きありがとうございました!
毎年、出版しているシリーズでしたが、雰囲気を一新したいことからコンペを使わせて頂きましたが、様々なデザイン提案を頂き、とても参考になりました。
今後もコンペを使わせて頂きますので、引き続きよろしくお願いいたします!

```html
<!DOCTYPE html>
<html lang="ja">
<head>
<meta charset="utf-8">
<title>Pebble magazine vol.5 2021</title>
<link rel="stylesheet" href="https://fonts.googleapis.com/css2?family=Noto+Sans+JP:wght@500;700;900&family=Montserrat:wght@500;700&display=swap">
<style>
  :root {
    --sky: #7cc6ea;
    --navy: #16365a;
    --white: #ffffff;
    --pink: #e8558a;
    --tick: #e03a3a;
    --band: #5b6771;
    --kit-light: rgba(255, 255, 255, 0.16);
    --kit-deep: rgba(255, 255, 255, 0.06);
  }
  * { margin: 0; padding: 0; box-sizing: border-box; }
  html, body { width: 750px; height: 1200px; overflow: hidden; }
  body { background: var(--sky); font-family: "Noto Sans JP", sans-serif; }
  .cover { position: relative; width: 750px; height: 1200px; background: var(--sky); }

  .masthead { position: absolute; left: 28px; top: 18px; color: var(--navy); }
  .masthead__kana { font-size: 15px; font-weight: 700; letter-spacing: 2px; margin-left: 70px; }
  .masthead__title { font-size: 82px; font-weight: 900; line-height: 0.95; }
  .masthead__sub { font-size: 50px; font-weight: 900; line-height: 1; margin-left: 6px; }

  .topics { position: absolute; left: 462px; top: 22px; list-style: none; color: var(--white); }
  .topics li { display: flex; align-items: flex-start; font-size: 27px; font-weight: 700; line-height: 1.3; margin-bottom: 10px; }
  .topics li::before { content: ""; flex: none; width: 20px; height: 20px; background: var(--pink); margin: 8px 10px 0 0; }

  .headline { position: absolute; left: 0; right: 0; top: 278px; text-align: center; color: var(--navy); font-size: 58px; font-weight: 900; line-height: 1.2; letter-spacing: 2px; }

  .headline-en { position: absolute; left: 0; right: 0; top: 448px; text-align: center; color: var(--white); font-family: "Montserrat", sans-serif; font-size: 23px; font-weight: 500; line-height: 1.3; letter-spacing: 1px; }

  .year { position: absolute; left: 0; right: 0; top: 512px; text-align: center; color: var(--navy); font-family: "Montserrat", sans-serif; font-size: 62px; font-weight: 700; line-height: 1; letter-spacing: 2px; }

  .bonus { position: absolute; left: 0; right: 0; top: 582px; display: flex; justify-content: center; align-items: center; gap: 8px; color: var(--white); font-size: 27px; font-weight: 700; }
  .bonus svg { width: 30px; height: 30px; }

  .kit-art { position: absolute; left: 38px; top: 640px; width: 674px; height: 430px; background: linear-gradient(180deg, var(--kit-light), var(--kit-deep)); border-radius: 4px; }

  .author { position: absolute; right: 40px; top: 1082px; color: var(--navy); font-size: 22px; font-weight: 700; letter-spacing: 2px; }

  .feature { position: absolute; left: 0; top: 1126px; width: 750px; height: 52px; background: var(--band); color: var(--white); display: flex; align-items: center; justify-content: center; font-size: 32px; font-weight: 700; letter-spacing: 2px; }
</style>
</head>
<body>
<main class="cover">
  <header class="masthead">
    <div class="masthead__kana">ペブル マガジン vol.5 2021</div>
    <div class="masthead__title">Pebble</div>
    <div class="masthead__sub">magazine</div>
  </header>

  <ul class="topics">
    <li>家づくりの補助金</li>
    <li>4月に省エネ説明<br>義務化</li>
    <li>IoT住宅の現在</li>
  </ul>

  <h1 class="headline">後悔しない住まい手配<br>ガイド決定版</h1>
  <p class="headline-en">a no-regret guide to<br>planning your own home</p>
  <p class="year">2021</p>

  <p class="bonus">
    <svg viewBox="0 0 30 30" aria-hidden="true">
      <rect x="2" y="4" width="24" height="24" fill="var(--white)"/>
      <path d="M6 15 L13 22 L28 4" fill="none" stroke="var(--tick)" stroke-width="4" stroke-linecap="round" stroke-linejoin="round"/>
    </svg>
    コロナ対応住宅チェックリスト付き!
  </p>

  <div class="kit-art" role="img" aria-label="プラモデルの部品枠「MY OWN HOUSE」に家・窓・ドア・家具・木などのパーツが並ぶイラスト"></div>

  <p class="author">一級建築士 柚木湊</p>

  <div class="feature">[特集] 三世代でつなぐ暮らし設計</div>
</main>
</body>
</html>
```